Aesthetics Company Flyer (description of services)

We need a 5.5"x8.5" flyer describing the services we offer at velvet horizon aesthetics. We are an aesthetics company located in Conroe TX. Our products and services can be found at www.vhaesthetics-demo.com/services . We would like to see designs that are cohesive with our brand and website: https://www.vhaesthetics-demo.com/

```html
<!DOCTYPE html>
<html lang="en">
<head>
<meta charset="utf-8">
<title>Velvet Horizon Aesthetics – Services</title>
<link href="https://fonts.googleapis.com/css2?family=Oswald:wght@300;400&family=Roboto+Condensed:wght@300;400&display=swap" rel="stylesheet">
<style>
:root{
  --ink:#333338;
  --white:#ffffff;
  --blush:#f6dbe3;
  --blush-soft:#fbecf1;
  --sky:#a8d8ec;
  --sky-line:#6cc4e6;
  --rose:#e9609a;
  --orchid:#b077ad;
  --petal:#f4c3cf;
  --gold:#f2d98c;
  --lilac:#c5b5d8;
  --plum:#8a6a9a;
  --mauve:#b784a7;
  --bullet:#1ea1dc;
}
*{box-sizing:border-box;margin:0;padding:0}
html,body{width:776px;height:1200px;overflow:hidden;background:var(--white)}
.flyer{position:relative;width:776px;height:1200px;overflow:hidden;background:var(--white);font-family:"Roboto Condensed",Arial,sans-serif;color:var(--ink)}
.backdrop{position:absolute;inset:0;width:776px;height:1200px}
.service-photo{position:absolute;width:303px;height:252px;border:2px solid;border-radius:70px 0 0 0;overflow:hidden}
.service-photo .fill{position:absolute;inset:0}
.service-title{position:absolute;left:16px;bottom:10px;font-family:"Oswald",sans-serif;font-weight:400;font-size:44px;line-height:46px;color:var(--white);letter-spacing:-0.5px;text-shadow:0 1px 3px rgba(0,0,0,.25)}
.service-title small{font-size:17px;color:var(--bullet);text-shadow:0 0 3px #fff;vertical-align:middle;margin-left:6px}
.fillers{left:70px;top:70px;border-color:var(--sky-line)}
.fillers .fill{background:linear-gradient(135deg,#e3b9a3,#c99883 55%,#8cc9e6)}
.fgf{left:399px;top:70px;border-color:var(--orchid)}
.fgf .fill{background:linear-gradient(135deg,#e7c6b6,#f0e6e4 55%,#d4b0a8)}
.pen{left:70px;top:640px;border-color:var(--gold)}
.pen .fill{background:linear-gradient(135deg,#c79d7a,#e9cdb9 55%,#d8b295)}
.peel{left:399px;top:640px;border-color:var(--lilac)}
.peel .fill{background:linear-gradient(135deg,#3a3a3a,#e5c83a 45%,#f1e07a 70%,#e8e2e6)}
.service-text{position:absolute;width:312px;font-size:19.5px;line-height:28.5px;font-weight:400}
.service-text .tag{display:inline-block;width:48px;height:14px;margin-right:6px;vertical-align:1px}
.fillers-text{left:70px;top:341px}
.fgf-text{left:400px;top:341px}
.pen-text{left:70px;top:911px}
.peel-text{left:400px;top:911px}
.area-list{list-style:none;margin-top:14px}
.area-list li{color:var(--mauve);font-size:19.5px;line-height:28px;text-transform:uppercase}
.area-list li::before{content:"";display:inline-block;width:9px;height:9px;background:var(--bullet);margin-right:6px;vertical-align:2px}
.contact{position:absolute;right:60px;top:1050px;text-align:right;color:var(--plum);font-family:"Oswald",sans-serif}
.phone{font-size:46px;line-height:52px;font-weight:400;letter-spacing:1px}
.email{font-family:"Roboto Condensed",sans-serif;font-size:19px;line-height:22px}
.website{position:absolute;right:40px;top:1128px;font-family:"Oswald",sans-serif;font-weight:400;font-size:45px;letter-spacing:5.5px;color:var(--plum)}
</style>
</head>
<body>
<main class="flyer">
  <svg class="backdrop" viewBox="0 0 776 1200" aria-hidden="true">
    <defs>
      <linearGradient id="blushWash" x1="0" y1="0" x2="1" y2="0">
        <stop offset="0" stop-color="#f6dbe3"/>
        <stop offset="1" stop-color="#fbecf1" stop-opacity="0.3"/>
      </linearGradient>
    </defs>
    <path d="M0 290 C120 300 260 360 420 330 C560 305 680 300 776 330 L776 560 C640 520 520 560 380 600 C240 640 120 610 0 560 Z" fill="url(#blushWash)" opacity="0.7"/>
    <path d="M0 260 C160 280 300 300 776 230 L776 290 C520 320 300 340 0 300 Z" fill="#f6dbe3" opacity="0.55"/>
    <path d="M0 1130 C200 1080 420 1000 776 1010 L776 1200 L0 1200 Z" fill="url(#blushWash)" opacity="0.7"/>
    <path d="M0 1140 C260 1180 500 1150 776 1170 L776 1200 L0 1200 Z" fill="#f6dbe3" opacity="0.6"/>
  </svg>

  <section class="service-photo fillers">
    <div class="fill" role="img" aria-label="Photo of a man's face marked for dermal filler treatment, gloved hand at the cheek"></div>
    <h2 class="service-title">Dermal Fillers</h2>
  </section>
  <div class="service-text fillers-text">
    <p><span class="tag" style="background:var(--sky)"></span>Dermal filler treatments plump up smile and frown lines, thin lips, and decrease cheek wrinkles and chin folds with FDA-approved volumizing hyaluronic acid, thus allow skin to restore fullness from the inside out.</p>
    <ul class="area-list">
      <li>Lips</li>
      <li>Smile lines/nasolabial folds</li>
    </ul>
  </div>

  <section class="service-photo fgf">
    <div class="fill" role="img" aria-label="Photo of a woman receiving a facial injection treatment"></div>
    <h2 class="service-title">Fibrin Growth<br>Factor<small>(FGF)</small></h2>
  </section>
  <p class="service-text fgf-text"><span class="tag" style="background:var(--rose)"></span>Fibrin Growth Factor (FGF) facial treatment enhances skin rejuvenation, scar and wound rejuvenation, and hair restoration by injecting plasma rich fibrin into the face. This component of contains fibrin growth factors and proteins that enhance cellular healing, rejuvenate tone, and promote new collagen growth.</p>

  <section class="service-photo pen">
    <div class="fill" role="img" aria-label="Photo of a microneedling pen used on a woman's forehead"></div>
    <h2 class="service-title">VelvaPen®</h2>
  </section>
  <p class="service-text pen-text"><span class="tag" style="background:var(--petal)"></span>VelvaPen® is a microneedling treatment that generates the skin’s self-repair mechanism and activates collagen and elastin production. Microneedling is great for scarring, problems with texture, enlarged pores, and even stretch marks.</p>

  <section class="service-photo peel">
    <div class="fill" role="img" aria-label="Photo of a yellow chemical peel being brushed onto a client's face"></div>
    <h2 class="service-title">Chemical Peels</h2>
  </section>
  <p class="service-text peel-text"><span class="tag" style="background:var(--lilac)"></span>Chemical Peels improve skin texture correcting pigmentation concerns, sun damage, and scarring.</p>

  <address class="contact" style="font-style:normal">
    <div class="phone">936 555 0142</div>
    <div class="email">maya@vhaesthetics-demo.com</div>
  </address>
  <div class="website">www.vhaesthetics-demo.com</div>
</main>
</body>
</html>
```